Forest Consultant/Timber Buyer needs a clean business card

We are a forestry consulting and timber buying company. We meet with private landowners and assist them with timber management and timber harvesting. We would like a professional business card, please no clip art. logo is blue and white but would like to see a gray,silver, or some other color incorporated. Would like basic contact info. Would like to the layout to be creative and sleek but masculine.

Target Market(s)

private landowners

Industry/Entity Type

Business

Contact Information for Business Card

name,position, cell number, office number, email, website. This might be to cluttered. Basic contact info is what we are looking for.

Contact info can all be on one side with logo on the other.

Font styles to use
Serif
Sans Serif

Colors
0255a3
ffffff
aaaaaa

Requirements
Must have
• We just want it professional.
Nice to have
• Creative layout.
Should not have
• please no clip art of log trucks etc.

```html
<!DOCTYPE html>
<html lang="en">
<head>
<meta charset="utf-8">
<title>Heritage Ridge Forestry – Business Card</title>
<link href="https://fonts.googleapis.com/css2?family=Open+Sans:wght@400;600;700&display=swap" rel="stylesheet">
<style>
  :root {
    --brand-blue: #0255a3;
    --card-white: #ffffff;
    --muted-gray: #aaaaaa;
    --stage: #d9dbde;
  }
  * { margin: 0; padding: 0; box-sizing: border-box; }
  html, body {
    width: 1200px; height: 900px; overflow: hidden;
    background: var(--stage);
    font-family: "Open Sans", Arial, sans-serif;
  }
  .canvas { position: relative; width: 1200px; height: 900px; }
  .card {
    position: absolute; left: 320px;
    width: 560px; height: 320px;
    border-radius: 22px;
    box-shadow: 0 10px 28px rgba(0,0,0,0.18);
    overflow: hidden;
  }
  .card-front { top: 100px; background: var(--brand-blue); }
  .card-back { top: 480px; background: var(--card-white); }

  .front-mark {
    position: absolute; inset: 0;
    display: flex; align-items: center; justify-content: center; gap: 18px;
  }
  .front-dot {
    width: 34px; height: 34px; border-radius: 50%;
    background: var(--card-white); flex: none;
  }
  .front-name {
    color: var(--card-white); font-weight: 700;
    font-size: 30px; letter-spacing: 1px; text-transform: uppercase;
    white-space: nowrap;
  }

  .back-mark {
    position: absolute; left: 30px; top: 130px;
    display: flex; align-items: center; gap: 10px;
  }
  .back-dot {
    width: 24px; height: 24px; border-radius: 50%;
    background: var(--brand-blue); flex: none;
  }
  .back-name {
    color: var(--brand-blue); font-weight: 700;
    font-size: 15px; letter-spacing: 0.3px; text-transform: uppercase;
    white-space: nowrap;
  }

  .divider {
    position: absolute; left: 322px; top: 70px;
    width: 1px; height: 120px;
    background: linear-gradient(var(--muted-gray), transparent);
  }
  .contact { position: absolute; left: 338px; top: 72px; }
  .person-name {
    color: var(--brand-blue); font-weight: 700; font-size: 19px;
    text-transform: uppercase; letter-spacing: 0.5px; line-height: 1.1;
    white-space: nowrap;
  }
  .person-role {
    color: var(--muted-gray); font-size: 10px; letter-spacing: 1px;
    text-transform: uppercase; margin-bottom: 10px;
  }
  .contact-list { list-style: none; }
  .contact-list li {
    display: flex; align-items: center; gap: 8px;
    color: var(--brand-blue); font-size: 13px; line-height: 17px;
    white-space: nowrap;
  }
  .contact-list svg { width: 10px; height: 10px; flex: none; }
</style>
</head>
<body>
<div class="canvas">
  <section class="card card-front">
    <div class="front-mark">
      <span class="front-dot"></span>
      <span class="front-name">Heritage Ridge Forestry</span>
    </div>
  </section>

  <section class="card card-back">
    <div class="back-mark">
      <span class="back-dot"></span>
      <span class="back-name">Heritage Ridge Forestry</span>
    </div>
    <div class="divider"></div>
    <div class="contact">
      <p class="person-name">Dale Harmon</p>
      <p class="person-role">Director</p>
      <ul class="contact-list">
        <li>
          <svg viewBox="0 0 10 10"><path d="M2 1 L4 3 L3 4 Q4 6 6 7 L7 6 L9 8 L8 9 Q3 9 1 2 Z" fill="#aaaaaa"/></svg>
          +330 5180-2264
        </li>
        <li>
          <svg viewBox="0 0 10 10"><rect x="2.5" y="0.5" width="5" height="9" rx="1" fill="#aaaaaa"/><rect x="3.3" y="1.5" width="3.4" height="5.5" fill="#ffffff"/><circle cx="5" cy="8.2" r="0.6" fill="#ffffff"/></svg>
          +330 5180-9931
        </li>
        <li>
          <svg viewBox="0 0 10 10"><rect x="0.5" y="2" width="9" height="6" fill="none" stroke="#aaaaaa"/><path d="M0.5 2 L5 5.5 L9.5 2" fill="none" stroke="#aaaaaa"/></svg>
          info@heritageridge.com
        </li>
        <li>
          <svg viewBox="0 0 10 10"><circle cx="5" cy="5" r="4.3" fill="none" stroke="#aaaaaa"/><path d="M0.7 5 H9.3 M5 0.7 V9.3" stroke="#aaaaaa"/></svg>
          www.heritageridge.com
        </li>
      </ul>
    </div>
  </section>
</div>
</body>
</html>
```